Business Card Design for Property Development Company Director

I am looking for a professional and unforgettable business card design for our Director of our Property Development Company.
Please see attached .pptx file to find out what information to include. You don't have to follow the exact format shown in the file - I am interested to see your creative flair using the information provided.

```html
<!DOCTYPE html>
<html lang="en">
<head>
<meta charset="utf-8">
<title>Harbrook Property Group – Business Card</title>
<link href="https://fonts.googleapis.com/css2?family=Montserrat:wght@400;500;700;800&display=swap" rel="stylesheet">
<style>
  :root {
    --brand-blue: #0d4f9e;
    --ink-grey: #4a4a4a;
    --soft-grey: #6b6b6b;
    --card-white: #f7f7f7;
    --stage: #d9dadc;
    --on-blue: #f2f4f8;
  }
  * { box-sizing: border-box; margin: 0; padding: 0; }
  html, body { width: 1200px; height: 1021px; overflow: hidden; }
  body {
    background: var(--stage);
    font-family: "Montserrat", sans-serif;
    display: flex; flex-direction: column; align-items: center; justify-content: center;
    gap: 70px;
  }
  .card {
    width: 700px; height: 400px; position: relative;
    box-shadow: 0 6px 18px rgba(0,0,0,.18);
  }
  /* Back side */
  .card-back {
    background: var(--brand-blue); color: var(--on-blue);
    display: flex; flex-direction: column; align-items: center;
  }
  .back-brand {
    margin-top: 110px; display: flex; align-items: center; gap: 14px;
    font-weight: 800; font-size: 46px; letter-spacing: 2px;
  }
  .back-brand .mark-square { width: 26px; height: 26px; background: var(--on-blue); }
  .tagline {
    margin-top: 22px; text-align: center; font-size: 19px; line-height: 1.25; letter-spacing: .5px;
  }
  .offer {
    position: absolute; bottom: 48px; left: 0; right: 0; text-align: center;
    font-size: 16px; letter-spacing: .4px;
  }
  .offer strong { font-weight: 700; }
  /* Front side */
  .card-front { background: var(--card-white); }
  .front-brand {
    position: absolute; left: 56px; top: 140px; width: 250px;
    color: var(--brand-blue); font-weight: 700;
  }
  .front-brand .name { font-size: 34px; letter-spacing: 1px; line-height: 1; }
  .front-brand .sub { font-size: 15px; letter-spacing: 4.5px; margin-top: 6px; }
  .divider {
    position: absolute; left: 340px; top: 100px; width: 2px; height: 160px; background: var(--soft-grey);
  }
  .contact { position: absolute; left: 380px; top: 112px; }
  .person-name { color: var(--brand-blue); font-weight: 800; font-size: 26px; }
  .person-role { color: var(--ink-grey); font-size: 18px; margin-top: 2px; }
  .contact-list { list-style: none; margin-top: 20px; }
  .contact-list li {
    display: flex; align-items: center; gap: 10px; color: var(--ink-grey);
    font-size: 19px; line-height: 1.35;
  }
  .contact-list svg { width: 18px; height: 18px; flex: none; }
  .licence {
    position: absolute; bottom: 44px; left: 0; right: 0; text-align: center;
    color: var(--soft-grey); font-size: 19px;
  }
</style>
</head>
<body>
  <section class="card card-back">
    <div class="back-brand"><span class="mark-square"></span>HARBROOK</div>
    <p class="tagline">Property Development<br>&amp; Site Acquisition Specialists</p>
    <p class="offer">Ask me about our <strong>INVESTMENT &amp; PARTNERSHIP</strong> opportunities</p>
  </section>

  <section class="card card-front">
    <div class="front-brand">
      <div class="name">HARBROOK</div>
      <div class="sub">PROPERTY GROUP</div>
    </div>
    <div class="divider"></div>
    <div class="contact">
      <h1 class="person-name">Daniel Marsh</h1>
      <p class="person-role">Director</p>
      <ul class="contact-list">
        <li>
          <svg viewBox="0 0 24 24" fill="#0d4f9e"><path d="M6.6 10.8a15.1 15.1 0 0 0 6.6 6.6l2.2-2.2c.3-.3.7-.4 1-.2 1.1.4 2.3.6 3.6.6.6 0 1 .4 1 1V20c0 .6-.4 1-1 1A17 17 0 0 1 3 4c0-.6.4-1 1-1h3.5c.6 0 1 .4 1 1 0 1.3.2 2.5.6 3.6.1.3 0 .7-.2 1z"/></svg>
          0400 182 736
        </li>
        <li>
          <svg viewBox="0 0 24 24" fill="none" stroke="#0d4f9e" stroke-width="2"><rect x="2.5" y="5" width="19" height="14"/><path d="M2.5 5l9.5 8 9.5-8"/></svg>
          daniel@harbrook.com.au
        </li>
        <li>
          <svg viewBox="0 0 24 24" fill="none" stroke="#0d4f9e" stroke-width="1.8"><circle cx="12" cy="12" r="9.5"/><ellipse cx="12" cy="12" rx="4" ry="9.5"/><path d="M2.5 12h19M4 7h16M4 17h16"/></svg>
          www.harbrook.com.au
        </li>
      </ul>
    </div>
    <p class="licence">Real Estate Lic: 5190362 &amp; 5190363</p>
  </section>
</body>
</html>
```